Corporate Design für Sachverständigerbüro
Zielgruppe
freiberufliche Tätigkeit als öffentlich bestellter und vereidigter Sachverständiger
Erstellung von landwirtschaftlichen und insolvenzspezifischen Gutachten, betriebswirtschaftliche Beratung, Betriebsfortführung, Unternehmensbewertung
Zielgruppe: Insovenzverwalter, Rechtsanwälte, Steuerberater, Landwirte
Aufgabenstellung
Nennung des Names, der öffentlichen Bestellung sowie Sachverständigenbüro Harald Kessing;
Gerne dunkelgrüne Logoelemente; Logo eher schlicht; Deisign sollte Seriösität, Vertrauen und Fachkompetenz kommunizieren

```html
<!DOCTYPE html>
<html lang="de">
<head>
<meta charset="utf-8">
<title>Briefbogen – Sachverständigenbüro Harald Kessing</title>
<link rel="stylesheet" href="https://fonts.googleapis.com/css2?family=EB+Garamond:wght@400;600;700&display=swap">
<style>
  :root {
    --backdrop: #ececec;
    --paper: #f3f2f3;
    --ink: #1e1e1e;
    --ink-soft: #3a3a3a;
    --forest: #0a5a3a;
    --forest-deep: #00392a;
  }
  * { box-sizing: border-box; margin: 0; padding: 0; }
  html, body {
    width: 1200px;
    height: 842px;
    overflow: hidden;
    background: var(--backdrop);
  }
  .letterhead {
    position: absolute;
    left: 360px;
    top: 92px;
    width: 465px;
    height: 657px;
    background: var(--paper);
    box-shadow: 2px 3px 10px rgba(0, 0, 0, 0.18);
    font-family: "EB Garamond", Garamond, serif;
    color: var(--ink);
  }
  .brand {
    position: absolute;
    left: 22px;
    top: 22px;
    display: flex;
    align-items: flex-start;
    gap: 4px;
  }
  .brand-square {
    width: 34px;
    height: 34px;
    background: var(--forest);
    flex: none;
  }
  .brand-text {
    line-height: 1;
    margin-top: -1px;
  }
  .brand-line {
    display: block;
    font-size: 8.4px;
    line-height: 9.6px;
  }
  .brand-name {
    display: block;
    font-size: 11.6px;
    font-weight: 600;
    letter-spacing: 0.1px;
    line-height: 12px;
    margin-top: 0.5px;
  }
  .brand-appointment {
    display: block;
    font-size: 3.9px;
    line-height: 5px;
    white-space: nowrap;
  }
  .contact {
    position: absolute;
    top: 23px;
    left: 0;
    width: 465px;
    font-size: 6.9px;
    line-height: 8.8px;
    font-style: normal;
  }
  .contact-online {
    position: absolute;
    right: 111px;
    text-align: right;
    font-weight: 600;
    white-space: nowrap;
  }
  .contact-divider {
    position: absolute;
    left: 360px;
    top: 0;
    width: 1px;
    height: 34px;
    background: var(--forest-deep);
  }
  .contact-postal {
    position: absolute;
    left: 366px;
    white-space: nowrap;
    color: var(--ink-soft);
  }
  .contact-label {
    display: inline-block;
    width: 15px;
  }
  .footer-band {
    position: absolute;
    left: 0;
    bottom: 0;
    width: 465px;
    height: 11px;
    display: block;
  }
</style>
</head>
<body>
  <main class="letterhead">
    <header class="brand">
      <div class="brand-square"></div>
      <div class="brand-text">
        <span class="brand-line">Dipl.-Ing. Agrar und</span>
        <span class="brand-line">Sachverständigenbüro</span>
        <span class="brand-name">HARALD KESSING</span>
        <span class="brand-appointment">Öffentlich bestellter und vereidigter Sachverständiger</span>
      </div>
    </header>

    <address class="contact">
      <div class="contact-online">
        kontakt@kessing-gutachten.de<br>
        www.kessing-gutachten.de
      </div>
      <div class="contact-divider"></div>
      <div class="contact-postal">
        Address<br>
        <span class="contact-label">Tel.</span> +49 (0)5141.876-210<br>
        <span class="contact-label">Fax.</span> +49 (0)5141.876-219<br>
        <span class="contact-label">Mob.</span>+49 (0)1578.462-905
      </div>
    </address>

    <svg class="footer-band" viewBox="0 0 465 11" preserveAspectRatio="none" aria-hidden="true">
      <rect x="0" y="0" width="465" height="11" fill="var(--forest-deep)"/>
      <polygon points="380,0 389,0 377,11 368,11" fill="var(--paper)"/>
      <polygon points="430,0 439,0 427,11 418,11" fill="var(--paper)"/>
    </svg>
  </main>
</body>
</html>
```